lantern productions business cards design

design a clean look but creative business card for a production company, I'm a freelance producer and launching my startup, would like to keep a clean professional look but still creative

Target Market(s)

businesses

Industry/Entity Type

video production

Contact Information for Business Card

logo, name (Mark Ellis), Title (Producer), (MFA Filmmaking, CSPT Los Angeles), contact number & email ID

Colors

Designer to choose only greyscale colors for use in the design.

Requirements
Must have
• logo, black and white colors, you can play with their shades
Nice to have
• a unique design, not necessarily a typical size card
Should not have
• too colorful or playful

```html
<!DOCTYPE html>
<html lang="en">
<head>
<meta charset="utf-8">
<title>Lantern Productions – Business Cards</title>
<link href="https://fonts.googleapis.com/css2?family=Montserrat:wght@400;600;700&family=Arimo:wght@400;700&display=swap" rel="stylesheet">
<style>
  :root {
    --stage: #2a2a2a;
    --ink: #0d0d0d;
    --paper: #ffffff;
    --card-black: #060606;
    --pattern-tone: #1c1e1d;
    --pattern-deep: #0b0b0b;
    --muted: #6b6b6b;
    --soft: #8a8a8a;
  }
  * { margin: 0; padding: 0; box-sizing: border-box; }
  html, body {
    width: 1200px; height: 900px; overflow: hidden;
    background: var(--stage);
  }
  .canvas {
    position: relative; width: 1200px; height: 900px;
  }
  .card {
    position: absolute; left: 250px; width: 700px; height: 400px;
    box-shadow: 0 12px 30px rgba(0,0,0,0.45);
  }
  /* Back side */
  .card-back {
    top: 40px;
    background: var(--card-black);
    overflow: hidden;
  }
  .card-back .pattern-field {
    position: absolute; inset: 0;
    background:
      radial-gradient(ellipse at 30% 45%, var(--pattern-tone) 0%, var(--pattern-deep) 60%, var(--card-black) 100%);
  }
  .card-back .brand {
    position: absolute; left: 0; right: 0; top: 168px;
    display: flex; align-items: center; justify-content: center; gap: 12px;
    font-family: 'Montserrat', sans-serif; font-weight: 600;
    font-size: 28px; color: var(--paper); letter-spacing: 0.5px;
  }
  .brand-dot {
    width: 14px; height: 14px; border-radius: 50%; background: currentColor;
  }
  /* Front side */
  .card-front {
    top: 460px;
    background: var(--paper);
    color: var(--ink);
    font-family: 'Montserrat', sans-serif;
  }
  .card-front .brand {
    position: absolute; left: 0; width: 560px; top: 62px;
    display: flex; align-items: center; justify-content: center; gap: 14px;
    font-weight: 600; font-size: 40px; color: var(--ink);
  }
  .identity {
    position: absolute; right: 370px; top: 212px; text-align: right;
  }
  .identity .name {
    font-family: 'Arimo', sans-serif; font-weight: 700;
    font-size: 30px; line-height: 1;
  }
  .identity .title {
    font-family: 'Arimo', sans-serif; font-size: 15px;
    color: var(--muted); margin-top: 2px;
  }
  .divider {
    position: absolute; left: 352px; top: 180px;
    width: 3px; height: 100px; background: var(--ink);
  }
  .contacts {
    position: absolute; left: 385px; top: 196px;
    list-style: none;
    font-family: 'Arimo', sans-serif; font-size: 17px; color: var(--soft);
  }
  .contacts li {
    display: flex; align-items: center; gap: 22px; height: 26px;
  }
  .contacts svg { width: 16px; height: 16px; fill: var(--ink); }
  .credential {
    position: absolute; left: 0; right: 0; bottom: 50px; text-align: center;
    font-size: 22px; letter-spacing: 3px; font-weight: 400;
  }
  .credential strong { font-weight: 700; }
</style>
</head>
<body>
<main class="canvas">

  <section class="card card-back" aria-label="Card back">
    <div class="pattern-field" role="img" aria-label="Faint repeating brand pattern in dark grey on black"></div>
    <div class="brand"><span class="brand-dot"></span>lantern productions</div>
  </section>

  <section class="card card-front" aria-label="Card front">
    <div class="brand"><span class="brand-dot"></span>lantern productions</div>

    <div class="identity">
      <p class="name">Mark Ellis</p>
      <p class="title">Producer</p>
    </div>

    <div class="divider"></div>

    <ul class="contacts">
      <li>
        <svg viewBox="0 0 24 24" aria-hidden="true"><path d="M6.6 10.8a15.1 15.1 0 0 0 6.6 6.6l2.2-2.2c.3-.3.7-.4 1-.2 1.1.4 2.3.6 3.6.6.6 0 1 .4 1 1V20c0 .6-.4 1-1 1A17 17 0 0 1 3 4c0-.6.4-1 1-1h3.5c.6 0 1 .4 1 1 0 1.3.2 2.5.6 3.6.1.3 0 .7-.2 1z"/></svg>
        <span>0198 762453</span>
      </li>
      <li>
        <svg viewBox="0 0 24 24" aria-hidden="true"><path d="M2 5h20v14H2z M3.5 6.5 12 13l8.5-6.5" fill="none" stroke="#0d0d0d" stroke-width="2"/></svg>
        <span>info@lanternproductions.com</span>
      </li>
    </ul>

    <p class="credential"><strong>MFA</strong> FILMMAKING, <strong>CSPT</strong> LOS ANGELES</p>
  </section>

</main>
</body>
</html>
```